An PHL basketball and news website

With the frenzy of basketball activities and huge audience in the Americas and Europe. I am looking for a glossy website which deals on the events and happening of PHL basketball league. The website is to cover news, events, scores and interviews with professional basketballer. The website will also cover other basketball events around the world such as the GORU global hoops tournaments. My target audience are Americans. I will prefer bright colors for my website. There will be a category for live basketball matches. Also fans will also be able on comment on the news column under the news iteam.

```html
<!DOCTYPE html>
<html lang="en">
<head>
<meta charset="utf-8">
<title>Basketball – PHL League News</title>
<link rel="stylesheet" href="https://fonts.googleapis.com/css2?family=Questrial&family=Lato:wght@400;700&family=Open+Sans:wght@400;600;700&family=Tinos&display=swap">
<style>
:root{
  --blue:#0a3a96;
  --blue-bright:#1a4fc4;
  --ink:#222;
  --grey-text:#666;
  --nav:#474747;
  --hero-dark:#1c1f24;
  --hero-mid:#3a3f47;
  --footer:#030303;
  --line:#cfcfcf;
  --white:#fff;
}
*{box-sizing:border-box;margin:0;padding:0}
html,body{width:1200px;height:2416px;overflow:hidden;background:var(--white)}
body{position:relative;font-family:"Lato",sans-serif;color:var(--ink)}
.abs{position:absolute}

/* Header */
.header{left:0;top:0;width:1200px;height:105px;background:var(--white)}
.header-icons{left:96px;top:34px;display:flex;gap:12px}
.header-icon{width:40px;height:40px;border:2px solid #bbb;border-radius:50%;display:flex;align-items:center;justify-content:center}
.brand{left:0;width:1200px;top:22px;text-align:center;font-family:"Questrial",sans-serif;font-size:56px;color:var(--blue);letter-spacing:1px}
.live-btn{left:888px;top:29px;width:260px;height:52px;background:var(--blue);color:var(--white);font-family:"Open Sans",sans-serif;font-weight:700;font-size:22px;display:flex;align-items:center;justify-content:center;box-shadow:inset 0 0 0 2px #2a5ad0}

/* Nav */
.nav{left:0;top:105px;width:1200px;height:69px;background:var(--nav);display:flex;align-items:center;font-family:"Open Sans",sans-serif;font-size:13.5px;font-weight:600;color:var(--white)}
.nav a{color:var(--white);text-decoration:none;position:absolute;top:0;height:69px;line-height:69px;transform:translateX(-50%)}
.nav .active{background:var(--blue);width:84px;text-align:center}

/* Hero */
.hero{left:0;top:174px;width:1200px;height:564px;background:radial-gradient(ellipse at 65% 30%,var(--hero-mid),var(--hero-dark) 70%)}
.hero-photo{left:80px;top:0;width:640px;height:564px;background:linear-gradient(180deg,#2b2c30,#141416);opacity:.75}
.hero-title{left:620px;top:100px;font-family:"Questrial",sans-serif;font-size:68px;color:var(--white)}
.hero-text{left:623px;top:192px;width:520px;font-size:13.5px;line-height:22px;color:var(--white)}
.hero-btn{left:625px;top:277px;width:142px;height:43px;border:1.5px solid #6f8fd8;background:var(--blue);color:var(--white);font-family:"Open Sans",sans-serif;font-size:12.5px;display:flex;align-items:center;justify-content:center}

/* Stories */
.story{width:528px}
.story-photo{width:528px;height:232px;background:linear-gradient(160deg,#6d5a4c,#2d3d7a 60%,#c5b7a8)}
.story-title{margin-top:18px;font-family:"Tinos",serif;font-size:17.5px;line-height:24px;color:var(--ink)}
.story-text{margin-top:8px;font-size:12.5px;line-height:22px;color:var(--grey-text)}
.story-text .more{display:inline-block;width:13px;height:13px;border-radius:50%;background:var(--blue);vertical-align:-2px;margin-left:10px;position:relative}
.story-text .more::after{content:"";position:absolute;left:3px;top:4px;border:3px solid transparent;border-left:5px solid var(--white)}

/* Video */
.video{left:0;top:1165px;width:1200px;height:430px;background:linear-gradient(180deg,#0e1118,#1a1d24 60%,#0b0d12)}
.video-title{left:64px;top:22px;font-family:"Open Sans",sans-serif;font-weight:600;font-size:35px;color:var(--white)}
.video-rule{left:214px;top:52px;width:938px;height:1px;background:#777}
.video-rule-dot{left:209px;top:47px;width:11px;height:11px;border:1px solid #999;border-radius:50%;background:#1a1d24}
.video-tabs{left:738px;top:33px;display:flex;gap:30px;font-size:12px;color:#2f62d4}
.video-tabs .on{color:var(--white)}
.thumb{top:99px;width:240px;height:268px;border:3px solid #eee;background:#dcdcdc}
.thumb.faded{background:linear-gradient(180deg,#e7e7e7,#d4d4d4);opacity:.9}
.thumb.current{background:linear-gradient(180deg,#3a3f6a,#7a2b2b)}
.play{left:50%;top:50%;width:52px;height:52px;margin:-26px 0 0 -26px;border-radius:50%;background:rgba(220,40,40,.85);border:2px solid rgba(255,255,255,.8)}
.play::after{content:"";position:absolute;left:19px;top:13px;border:11px solid transparent;border-left:17px solid var(--white);border-right:0}
.slide-arrow{top:207px;width:30px;height:30px;border:1.5px solid #ddd;border-radius:50%}

/* Testimonials */
.testi-head{left:0;top:1614px;width:1200px;text-align:center;font-family:"Open Sans",sans-serif;font-weight:600;font-size:32px;color:var(--ink)}
.testi-head span{color:var(--blue)}
.quote-box{left:335px;top:1707px;width:422px;height:171px;border:1.5px solid #e4e4e4;padding:38px 26px 0 22px;font-size:12px;line-height:22.5px;color:#9a9a9a;font-style:italic}
.avatar{left:777px;top:1712px;width:80px;height:80px;border-radius:50%;border:2px solid #555;background:linear-gradient(180deg,#d9d9d9,#8c8c8c)}
.person{left:737px;top:1800px;width:160px;text-align:center}
.person-name{font-family:"Open Sans",sans-serif;font-weight:600;font-size:19px;color:var(--blue)}
.person-city{font-size:11px;color:#888;margin-top:2px}

/* Footer */
.footer{left:0;top:1925px;width:1200px;height:414px;background:var(--footer);color:var(--white)}
.col-head{font-family:"Open Sans",sans-serif;font-weight:600;font-size:22px;color:var(--blue-bright)}
.dots{height:0;border-top:2px dotted #888}
.view-all{font-size:11px;color:var(--white)}
.col-divider{top:68px;width:1px;height:298px;background:#333}
.about-text{left:48px;top:97px;width:255px;font-size:14.5px;line-height:22.5px;text-align:justify}
.read-more{left:52px;top:264px;font-size:14px;color:var(--blue-bright)}
.badge{top:322px;width:52px;height:54px;background:#e8e8e8}
.item{display:flex;gap:14px;height:48px}
.item-thumb{width:50px;height:48px;background:linear-gradient(160deg,#6b4c3a,#26335e);flex:none}
.item-title{font-size:14px;color:var(--blue-bright);line-height:16px}
.item-text{font-size:11.5px;line-height:15.5px;color:var(--white)}
.news-date{width:40px;font-size:16px;line-height:20px;color:var(--blue-bright);text-align:center;padding-top:6px;flex:none}

/* Bottom bar */
.bar{left:0;top:2339px;width:1200px;height:77px;background:var(--blue)}
.copyright{left:0;width:1240px;top:30px;text-align:center;font-size:11.5px;color:var(--white)}
.social{top:23px;width:28px;height:28px;border:1.5px solid var(--white)}
</style>
</head>
<body>

<header class="header abs">
  <div class="header-icons abs">
    <span class="header-icon"><svg width="16" height="18" viewBox="0 0 16 18"><path d="M8 1a5.5 5.5 0 0 0-5.5 5.5C2.5 11 8 17 8 17s5.5-6 5.5-10.5A5.5 5.5 0 0 0 8 1z" fill="none" stroke="#999" stroke-width="1.6"/><circle cx="8" cy="6.5" r="2" fill="#999"/></svg></span>
    <span class="header-icon"><svg width="16" height="16" viewBox="0 0 16 16"><path d="M3.5 1.5l3 3-1.8 1.8a9 9 0 0 0 5 5L11.5 9.5l3 3-2 2C6.5 14 2 9.5 1.5 3.5z" fill="none" stroke="#999" stroke-width="1.5" stroke-linejoin="round"/></svg></span>
    <span class="header-icon"><svg width="16" height="16" viewBox="0 0 16 16"><circle cx="6.5" cy="6.5" r="4.5" fill="none" stroke="#999" stroke-width="1.8"/><path d="M10 10l4.5 4.5" stroke="#999" stroke-width="2"/></svg></span>
  </div>
  <div class="brand abs">Basketball</div>
  <a class="live-btn abs">Today Match Live</a>
</header>

<nav class="nav abs">
  <a class="active" style="left:111px">HOME</a>
  <a style="left:211px">VIDEOS</a>
  <a style="left:317px">SCORES</a>
  <a style="left:432px">SCHEDULE</a>
  <a style="left:560px">STANDINGS</a>
  <a style="left:673px">STATS</a>
  <a style="left:769px">TEAMS</a>
  <a style="left:866px">NEWS</a>
  <a style="left:967px">MOBILE</a>
  <a style="left:1080px">CONNECT</a>
</nav>

<section class="hero abs">
  <div class="hero-photo abs" role="img" aria-label="Basketball player in a dark jersey dribbling a ball"></div>
  <h1 class="hero-title abs">South Power</h1>
  <p class="hero-text abs">Lorem ipsum dolor sit amet, consectetur adipiscing elit, sed do eiusmod tempor incididunt ut labore et dolore magna aliqua. Ut enim ad minim veniam, quis nostrud exercitation ullamco laboris</p>
  <a class="hero-btn abs">READ MORE</a>
</section>

<article class="story abs" style="left:47px;top:783px">
  <div class="story-photo" role="img" aria-label="Players in white and blue jerseys contesting the ball in front of a crowd"></div>
  <h2 class="story-title">Eastfield Pro Basketball League Season 2 Day 7: Rising Delhi and Bengaluru sides</h2>
  <p class="story-text">Lorem ipsum dolor sit amet, consectetur adipiscing elit, sed do eiusmod tempor incididunt ut labore et dolore magna aliqua. Ut enim ad minim veniam<span class="more"></span></p>
</article>
<article class="story abs" style="left:622px;top:783px">
  <div class="story-photo" style="background:linear-gradient(160deg,#7a5a3e,#d9b53a 40%,#2a3b6e 70%,#c8a27a)" role="img" aria-label="Player in a yellow jersey driving past a defender in blue"></div>
  <h2 class="story-title">Eastfield Pro Basketball League Season 2 Day 7: Rising Delhi and Bengaluru sides</h2>
  <p class="story-text">Lorem ipsum dolor sit amet, consectetur adipiscing elit, sed do eiusmod tempor incididunt ut labore et dolore magna aliqua. Ut enim ad minim veniam<span class="more"></span></p>
</article>

<section class="video abs" role="region" aria-label="Video">
  <h2 class="video-title abs">Video</h2>
  <div class="video-rule abs"></div>
  <div class="video-rule-dot abs"></div>
  <div class="video-tabs abs"><span class="on">Highlights</span><span>Top Plays</span><span>Editor's Picks</span><span>Channal</span><span>Watch Live</span></div>
  <div class="thumb faded abs" style="left:64px" role="img" aria-label="Video still of a player shooting under the basket"></div>
  <div class="thumb current abs" style="left:337px" role="img" aria-label="Video still of a player in red leaping for a dunk"><span class="play abs"></span></div>
  <div class="thumb faded abs" style="left:614px" role="img" aria-label="Video still of a player in white on court"></div>
  <div class="thumb faded abs" style="left:889px" role="img" aria-label="Video still of a player in blue dribbling"></div>
  <svg class="slide-arrow abs" style="left:17px" viewBox="0 0 30 30"><path d="M17 10l-5 5 5 5" fill="none" stroke="#fff" stroke-width="2"/></svg>
  <svg class="slide-arrow abs" style="left:1145px" viewBox="0 0 30 30"><path d="M13 10l5 5-5 5" fill="none" stroke="#fff" stroke-width="2"/></svg>
</section>

<h2 class="testi-head abs">Our <span>Testimonials</span></h2>
<svg class="abs" style="left:166px;top:1738px" width="42" height="112" viewBox="0 0 42 112"><path d="M40 2L3 56l37 54" fill="none" stroke="#c8c8c8" stroke-width="2"/></svg>
<svg class="abs" style="left:972px;top:1738px" width="42" height="112" viewBox="0 0 42 112"><path d="M2 2l37 54-37 54" fill="none" stroke="#c8c8c8" stroke-width="2"/></svg>
<div class="quote-box abs">Lorem ipsum dolor sit amet, consectetur adipiscing elit, sed do eiusmod tempor incididunt ut labore et dolore magna aliqua. Ut enim ad minim veniam, quis nostrud exercitation ullamco laboris nisi ut aliquip ex ea commodo consequat.</div>
<svg class="abs" style="left:327px;top:1696px" width="48" height="34" viewBox="0 0 48 34"><g fill="#d8d8d8"><path d="M2 32V18C2 8 8 2 18 1v6c-5 1-8 5-8 10h8v15z"/><path d="M26 32V18c0-10 6-16 16-17v6c-5 1-8 5-8 10h8v15z"/></g></svg>
<svg class="abs" style="left:694px;top:1856px" width="48" height="34" viewBox="0 0 48 34"><g fill="#d8d8d8"><path d="M46 2v14c0 10-6 16-16 17v-6c5-1 8-5 8-10h-8V2z"/><path d="M22 2v14c0 10-6 16-16 17v-6c5-1 8-5 8-10H6V2z"/></g></svg>
<svg class="abs" style="left:755px;top:1740px" width="20" height="20" viewBox="0 0 20 20"><path d="M0 0l18 10L0 20" fill="#fff" stroke="#e4e4e4" stroke-width="1.5"/></svg>
<div class="avatar abs" role="img" aria-label="Portrait of John Smith"></div>
<div class="person abs"><div class="person-name">John Smith</div><div class="person-city">City Location</div></div>

<footer class="footer abs">
  <h3 class="col-head abs" style="left:48px;top:28px">About Us</h3>
  <div class="dots abs" style="left:48px;top:72px;width:230px"></div>
  <p class="about-text abs">Lorem ipsum dolor sit amet, consectetur adipiscing elit, sed do eiusmod tempor incididunt ut labore et dolore magna aliqua. Ut enim ad minim veniam, quis nostrud exercitation ullamco laboris nisi ut aliquip ex ea commodo consequat.</p>
  <a class="read-more abs">Read More ›</a>
  <div class="abs" style="left:48px;top:300px;width:245px;height:1px;background:#333"></div>
  <div class="badge abs" style="left:48px"></div>
  <div class="badge abs" style="left:134px;border-radius:4px"></div>
  <div class="badge abs" style="left:215px;border-radius:50%;background:#b8283a"></div>

  <div class="col-divider abs" style="left:330px"></div>

  <h3 class="col-head abs" style="left:396px;top:30px">Events blog</h3>
  <span class="view-all abs" style="left:680px;top:57px">View All</span>
  <div class="dots abs" style="left:402px;top:74px;width:323px"></div>
  <div class="abs" style="left:406px;top:100px;width:320px">
    <div class="item"><div class="item-thumb" role="img" aria-label="Event photo"></div><div><div class="item-title">Lorem ipsum dolor sit ame</div><div class="item-text">Give up alcohol if cancer runs in your family, do Northgate study warns - The Daily Courier</div></div></div>
    <div class="dots" style="margin:20px 0 29px -4px;width:323px"></div>
    <div class="item"><div class="item-thumb" role="img" aria-label="Event photo"></div><div><div class="item-title">Lorem ipsum dolor sit ame</div><div class="item-text">Give up alcohol if cancer runs in your family, do Northgate study warns - The Daily Courier</div></div></div>
    <div class="dots" style="margin:20px 0 29px -4px;width:323px"></div>
    <div class="item"><div class="item-thumb" role="img" aria-label="Event photo"></div><div><div class="item-title">Lorem ipsum dolor sit ame</div><div class="item-text">Give up alcohol if cancer runs in your family, do Northgate study warns - The Daily Courier</div></div></div>
    <div class="dots" style="margin:20px 0 0 -4px;width:323px"></div>
  </div>

  <div class="col-divider abs" style="left:773px"></div>

  <h3 class="col-head abs" style="left:812px;top:28px">Latest News</h3>
  <span class="view-all abs" style="left:1092px;top:56px">View All</span>
  <div class="dots abs" style="left:812px;top:73px;width:325px"></div>
  <div class="abs" style="left:812px;top:103px;width:325px">
    <div class="item"><div class="news-date">17<br>Aug</div><div class="item-thumb" role="img" aria-label="News photo"></div><div class="item-text" style="padding-top:3px">Give up alcohol if cancer runs in your family, Northgate study warns - The Daily Courier</div></div>
    <div class="dots" style="margin:20px 0 29px 0"></div>
    <div class="item"><div class="news-date">17<br>Aug</div><div class="item-thumb" role="img" aria-label="News photo"></div><div class="item-text" style="padding-top:3px">Give up alcohol if cancer runs in your family, Northgate study warns - The Daily Courier</div></div>
    <div class="dots" style="margin:20px 0 29px 0"></div>
    <div class="item"><div class="news-date">17<br>Aug</div><div class="item-thumb" role="img" aria-label="News photo"></div><div class="item-text" style="padding-top:3px">Give up alcohol if cancer runs in your family, Northgate study warns - The Daily Courier</div></div>
    <div class="dots" style="margin:20px 0 0 0"></div>
  </div>
</footer>

<div class="bar abs">
  <p class="copyright abs">Copyright 2016 Company Name. All Rights Reserved.</p>
  <span class="social abs" style="left:1004px"></span>
  <span class="social abs" style="left:1043px"></span>
  <span class="social abs" style="left:1082px"></span>
  <span class="social abs" style="left:1121px"></span>
</div>

</body>
</html>
```